KBT Trifold

- Hello -
We are looking for an exciting trifold design for our residential roofing and interior remodeling company. Below is the website for more inspiration and images. We would like to include the Veteran Owned section somewhere on the back.

https://kestrelbuildingandtrades.example/

Thank You,
Elliot

```html
<!DOCTYPE html>
<html lang="en">
<head>
<meta charset="utf-8">
<title>KBT Trifold – Services Panel</title>
<link rel="stylesheet" href="https://fonts.googleapis.com/css2?family=Outfit:ital,wght@0,300;0,400;0,600;0,700;1,300;1,400&display=swap">
<style>
  :root{
    --maroon:#7d2f35;
    --quote-bg:#86363b;
    --ink:#262626;
    --pill:#8b8279;
    --line:#8a8a8a;
    --panel-tint:#f2f0ee;
    --paper:#ffffff;
  }
  *{box-sizing:border-box;margin:0;padding:0}
  html,body{width:1200px;height:855px;overflow:hidden;background:var(--paper)}
  body{font-family:"Outfit",Arial,sans-serif;color:var(--ink)}
  .sheet{position:relative;width:1200px;height:855px;background:var(--paper);overflow:hidden}
  .panel-tint{position:absolute;left:799px;top:0;width:401px;height:855px;background:var(--panel-tint)}
  .storm-bg{position:absolute;left:0;top:535px;width:449px;height:320px;
    background:linear-gradient(165deg,#ebe9e7 0%,#f6f5f4 30%,#e4e1df 55%,#f3f2f1 80%,#e9e7e5 100%)}
  .photo{position:absolute}
  .photo-roof{left:32px;top:29px;width:366px;height:235px;background:linear-gradient(160deg,#6e5e57 0%,#7b6b63 45%,#5c6a45 80%,#4b5b3a 100%)}
  .photo-kitchen{left:412px;top:29px;width:428px;height:235px;background:linear-gradient(90deg,#8d8378 0%,#b6aa9b 35%,#dcd7d0 60%,#c9bfb2 100%)}
  .photo-bath{left:856px;top:29px;width:315px;height:235px;background:linear-gradient(120deg,#bfc6c2 0%,#dde0de 50%,#efefec 100%)}
  .photo-kitchen-two{left:400px;top:535px;width:440px;height:290px;background:linear-gradient(170deg,#b9aa99 0%,#8f7a66 40%,#d9d7d4 70%,#a69a8c 100%)}
  .photo-bath-two{left:856px;top:492px;width:315px;height:333px;background:linear-gradient(110deg,#e6e3df 0%,#c9c2b8 40%,#ecebe8 70%,#b7b0a6 100%)}
  .heading{position:absolute;color:var(--maroon);font-weight:600;font-size:27px;line-height:26px;letter-spacing:.6px;text-transform:uppercase}
  .icon{position:absolute;fill:none;stroke:var(--line);stroke-width:1.3}
  .body{position:absolute;font-size:15.3px;line-height:21px;font-weight:300}
  .body b{font-weight:600}
  .pill{position:absolute;left:42px;top:348px;width:182px;height:22px;border-radius:11px;background:var(--pill);color:#fff;
    font-size:10.5px;font-weight:600;letter-spacing:3px;line-height:22px;padding-left:11px}
  .storm-kicker{position:absolute;left:44px;top:556px;font-size:16px;font-weight:600;letter-spacing:1px;color:var(--ink)}
  .storm-rule{position:absolute;left:44px;top:634px;width:322px;height:1.5px;background:var(--maroon)}
  .quote{position:absolute;left:419px;top:490px;width:361px;height:93px;background:var(--quote-bg);color:#fff;
    font-style:italic;font-weight:300;font-size:14px;line-height:19.5px;text-align:center;padding-top:16px}
</style>
</head>
<body>
<div class="sheet">
  <div class="panel-tint"></div>
  <div class="storm-bg"></div>

  <div class="photo photo-roof" role="img" aria-label="Aerial view of a house with a new shingle roof and landscaped front yard"></div>
  <div class="photo photo-kitchen" role="img" aria-label="Modern kitchen with wood cabinets, island with bar stools and large window"></div>
  <div class="photo photo-bath" role="img" aria-label="Marble bathroom with glass shower, soaking tub and arched window"></div>

  <h2 class="heading" style="left:44px;top:291px">Roofing,<br>Siding &amp; Gutter</h2>
  <svg class="icon" style="left:294px;top:287px" width="84" height="58" viewBox="0 0 84 58">
    <polyline points="1,26 19,2 36,26"/><polyline points="19,2 72,14 82,24"/><line x1="72" y1="14" x2="72" y2="56"/><line x1="72" y1="24" x2="82" y2="24"/>
  </svg>
  <div class="pill">LIFETIME WARRANTY</div>
  <p class="body" style="left:44px;top:383px;width:340px">Whether you’re looking to do roof repair, roof replacement, new gutters, new siding, trust our licensed professionals. We work with the top manufacturers in the industry <b>Corvane Summit Series Roofing System</b> – Gale Guard Shake, Crestline Pure.</p>

  <h2 class="heading" style="left:427px;top:291px">Kitchen<br>Remodeling</h2>
  <svg class="icon" style="left:694px;top:290px" width="74" height="54" viewBox="0 0 74 54">
    <rect x="1" y="1" width="27" height="52"/><rect x="28" y="20" width="45" height="33"/><line x1="28" y1="36" x2="73" y2="36"/>
    <line x1="6" y1="22" x2="6" y2="30"/><line x1="45" y1="41" x2="57" y2="41"/><line x1="45" y1="26" x2="57" y2="26"/>
    <path d="M47 20 V13 a5 5 0 0 1 10 0 V17"/>
  </svg>
  <p class="body" style="left:429px;top:363px;width:340px">Your kitchen is the central hub of every home. We’ll collaborate with you to make this space open and functional for everyone to enjoy. We use the latest building products and trends to meet and exceed your expectations.</p>

  <h2 class="heading" style="left:829px;top:291px">Bathroom<br>Remodeling</h2>
  <svg class="icon" style="left:1076px;top:296px" width="82" height="46" viewBox="0 0 82 46">
    <line x1="1" y1="12" x2="81" y2="12"/><path d="M4 12 Q8 34 24 34 H58 Q74 34 78 12"/>
    <line x1="18" y1="34" x2="16" y2="44"/><line x1="64" y1="34" x2="66" y2="44"/>
    <path d="M38 12 V4 H46 V8"/><line x1="33" y1="12" x2="33" y2="7"/><line x1="51" y1="12" x2="51" y2="7"/>
  </svg>
  <p class="body" style="left:829px;top:363px;width:345px"><b>Make It Picture Perfect!</b> Give your bathroom a new life and increase the value of your home at the same time. We offer full service design assistance to transform the bathroom into your very own spa retreat.</p>

  <div class="storm-kicker">STORM DAMAGE</div>
  <h2 class="heading" style="left:44px;top:581px">Renovation or<br>Restoration</h2>
  <div class="storm-rule"></div>
  <p class="body" style="left:44px;top:651px;width:330px;font-weight:400;font-size:15px">Time for new Roof, Siding or Gutters? Hail or Storm damage?&nbsp; We are here to assist in every aspect. <b>With decades of experience negotiating with Insurance companies</b> for accurate assessments, we work with the best trades for the project, and ensure your home is not only built well but looks just as beautiful.</p>

  <div class="photo photo-kitchen-two" role="img" aria-label="Kitchen with brick wall, white waterfall island and wire bar stools"></div>
  <div class="photo photo-bath-two" role="img" aria-label="Bathroom with freestanding tub, glass shower and black-framed window"></div>

  <blockquote class="quote">“I wake up every day excited to use my dream<br>kitchen. Thank you, Kestrel Building and<br>Trades!” - Dana Whitfield</blockquote>
</div>
</body>
</html>
```